Major Chiropractic Campaign Shown to 7 million people in print and online

Please design a SIMPLE and CLEAR advert in various sizes that will be used for print and media.

1/ Newspaper Print size: 381 x 272 with border and MUST be able to stand out in a newspaper

2/ Media: 5 sizes - rotating .gif 2 frames
- 160x600
- 728x90
- 300x250
- 300x600
- 320x50

3/ Facebook (must pass: http://ninetenthsgauge.info)
- 300x315

Target Market(s)

females
35 - 54 yo
educated

Industry/Entity Type

Media

Font styles to use
Sans Serif

Colors
3176b5
33a6d7
ffffff
ec1f27
1b1b1b
919191
9bcb3c

Requirements
Must have
• clean
• easy to read
• strong CALL TO ACTION
• professional
• well designed book cover with the title " The Quiet Pathway Linking Your Nerves and Posture Revealed"
• The book MUST look like it's a professional report
• the winning design WILL show all design on a single page

```html
<!DOCTYPE html>
<html lang="en">
<head>
<meta charset="utf-8">
<title>Free Report Advert</title>
<link rel="stylesheet" href="https://fonts.googleapis.com/css2?family=Josefin+Sans:wght@400;600;700&family=Oswald:wght@600&display=swap">
<style>
  :root {
    --brand-blue: #3176b5;
    --brand-sky: #33a6d7;
    --brand-red: #ec1f27;
    --brand-ink: #1b1b1b;
    --brand-grey: #919191;
    --brand-green: #9bcb3c;
    --white: #ffffff;
  }
  * { margin: 0; padding: 0; box-sizing: border-box; }
  html, body { width: 1200px; height: 900px; overflow: hidden; }
  .advert {
    position: relative;
    width: 1200px;
    height: 900px;
    overflow: hidden;
    background: radial-gradient(ellipse 560px 500px at 430px 420px, var(--brand-sky) 0%, var(--brand-blue) 100%);
    font-family: "Josefin Sans", sans-serif;
    color: var(--white);
  }
  .headline {
    position: absolute;
    top: 34px;
    left: 0;
    width: 1200px;
    text-align: center;
    font-weight: 400;
    font-size: 54px;
    line-height: 65px;
    letter-spacing: 5px;
    text-transform: uppercase;
  }
  .report-shadow {
    position: absolute;
    left: 420px;
    top: 742px;
    width: 420px;
    height: 58px;
    border-radius: 50%;
    background: radial-gradient(ellipse at center, rgba(27,27,27,0.55) 0%, rgba(27,27,27,0) 70%);
  }
  .report-pages {
    position: absolute;
    left: 760px;
    top: 256px;
    width: 40px;
    height: 510px;
    background: repeating-linear-gradient(90deg, var(--white) 0 3px, var(--brand-grey) 3px 4px);
  }
  .report-cover {
    position: absolute;
    left: 438px;
    top: 250px;
    width: 327px;
    height: 522px;
    background: var(--brand-ink);
    text-align: center;
  }
  .report-label {
    margin-top: 38px;
    font-weight: 700;
    font-size: 40px;
    letter-spacing: 2px;
    padding-left: 8px;
  }
  .report-band {
    position: absolute;
    left: 0;
    top: 95px;
    width: 327px;
    height: 262px;
    background: var(--brand-red);
  }
  .report-count {
    margin-top: 16px;
    font-family: "Oswald", sans-serif;
    font-weight: 600;
    font-size: 52px;
    line-height: 58px;
    letter-spacing: 1px;
    text-transform: uppercase;
  }
  .report-title {
    margin-top: 6px;
    font-size: 26px;
    line-height: 32px;
    letter-spacing: 1px;
    text-transform: uppercase;
  }
  .report-note {
    margin-top: 8px;
    font-size: 15px;
    letter-spacing: 1px;
    text-transform: uppercase;
  }
  .footer-band {
    position: absolute;
    left: 0;
    top: 800px;
    width: 1200px;
    height: 100px;
    background: var(--brand-ink);
  }
  .footer-label {
    position: absolute;
    left: 110px;
    top: 42px;
    font-size: 34px;
    letter-spacing: 3px;
    text-transform: uppercase;
    color: var(--brand-green);
  }
  .footer-url {
    position: absolute;
    left: 440px;
    top: 26px;
    font-size: 52px;
    letter-spacing: 3px;
  }
</style>
</head>
<body>
<main class="advert">
  <h1 class="headline">Doctor explains hidden<br>connection that controls<br>your health</h1>

  <div class="report-shadow"></div>
  <div class="report-pages"></div>
  <section class="report-cover">
    <p class="report-label">FREE REPORT</p>
    <div class="report-band">
      <p class="report-count">The Quiet<br>Pathway</p>
      <p class="report-title">Linking your<br>nerves and<br>posture revealed</p>
      <p class="report-note">(And what to do about it)</p>
    </div>
  </section>

  <footer class="footer-band">
    <span class="footer-label">Free Report</span>
    <span class="footer-url">www.learnmorenow.com.au</span>
  </footer>
</main>
</body>
</html>
```